Online Rug Store needs Clearance Banner

Website is: Lanternfield Carpets and Home
You can access it at: www.lanternfieldcarpetsandhome.com and login (top right) with password: trazok

*** update: When creating banners for my site, you have permission to use images from www.velbora.com, but ONLY for this project. The images/artwork are copyright allowable for use on www.lanternfieldcarpetsandhome.com projects.***

We need a home page banner sized 1000 wide x 500 tall pixels to promote a "Clearance Sale" on rugs. The banner can state:

1. Clearance Sale
2. Now in progress
3. Save an extra 20% with coupon code 'Mint20'
4. Ends March 31st
5. Plus Free Shipping and 30 day returns.

We prefer a banner that appears hand-drawn and artistic, not commercially produced. It is OK to use a room scene image, rug images, or just a colored/textured background with text and no images. Your choice.

Flat graphics with no shadows and 3-D effect preferred.
Attached is are 3 logo options, as well as an example banner with handcrafted, artistic styling that we prefer.

Target Market(s)

This should be an eye-catching banner to showcase a very urgent promotion. Consider using colors of red, white, gold, and black to make a strong statement on the home page.

Industry/Entity Type

Home And Garden

Requirements
Must have
• Winner must provide Photoshop editable file format (.psd format) including layers that can be edited.
Nice to have
• Hand-drawn, stenciled, scribbled, artistic graphics and fonts is nice because we sell rugs that are made by hand.
Should not have
• little to no shadowing. Avoid computerized graphics.

```html
<!DOCTYPE html>
<html lang="en">
<head>
<meta charset="utf-8">
<title>Lanternfield Carpets and Home</title>
<link href="https://fonts.googleapis.com/css2?family=Cinzel:wght@400&family=Lora:wght@400&family=Open+Sans:wght@400;700&family=Kaushan+Script&family=Permanent+Marker&display=swap" rel="stylesheet">
<style>
  :root {
    --page-bg: #ffffff;
    --ink: #1f1f1f;
    --muted-ink: #555555;
    --nav-band: #c9b48b;
    --nav-text: #ffffff;
    --field-bg: #efece6;
    --field-text: #8a8680;
    --banner-dark: #2b231d;
    --banner-mid: #4a3f33;
    --sale-coral: #e8835f;
    --banner-white: #ffffff;
    --link-soft: #9fb3c6;
    --dot: #9aa79b;
    --card-line: #cfcac2;
  }
  * { box-sizing: border-box; margin: 0; padding: 0; }
  html, body { width: 1200px; height: 1000px; overflow: hidden; background: var(--page-bg); }
  body { position: relative; font-family: "Open Sans", Arial, sans-serif; color: var(--ink); border-top: 1px solid #d8dde2; }

  .brand { position: absolute; left: 107px; top: 76px; display: flex; align-items: center; gap: 14px; }
  .brand-mark { width: 64px; height: 64px; background: #9b1c1c; }
  .brand-name { font-family: "Cinzel", Georgia, serif; font-weight: 400; color: #1a1a1a; line-height: 1.02; }
  .brand-name .line-one { display: block; font-size: 32px; letter-spacing: 1.5px; }
  .brand-name .line-two { display: block; font-size: 23px; letter-spacing: 1px; }

  .account-links { position: absolute; right: 54px; top: 46px; font-size: 14px; color: var(--muted-ink); text-align: right; line-height: 24px; }
  .account-links strong { color: #3a3a3a; font-weight: 700; }

  .search-field { position: absolute; left: 684px; top: 111px; width: 328px; height: 48px; background: var(--field-bg); border-radius: 2px; }
  .search-field span { position: absolute; left: 11px; top: 13px; font-family: "Lora", Georgia, serif; font-size: 16px; color: var(--field-text); }
  .search-field svg { position: absolute; right: 14px; top: 13px; }

  .cart-button { position: absolute; left: 1033px; top: 111px; width: 113px; height: 48px; background: var(--field-bg); border-radius: 2px; display: flex; align-items: center; justify-content: center; gap: 9px; font-family: "Lora", Georgia, serif; font-size: 17px; color: #555; }

  .main-nav { position: absolute; left: 0; top: 222px; width: 1200px; height: 61px; background: var(--nav-band); display: flex; align-items: center; padding-left: 53px; gap: 36px; }
  .main-nav a { font-family: "Lora", Georgia, serif; font-size: 17px; color: var(--nav-text); text-decoration: none; }

  .hero-banner { position: absolute; left: 53px; top: 315px; width: 1095px; height: 548px; overflow: hidden; background: radial-gradient(ellipse at center, var(--banner-mid) 0%, var(--banner-dark) 75%); }
  .hero-pattern { position: absolute; inset: 0; }
  .sale-title { position: absolute; left: 0; width: 100%; top: 110px; text-align: center; font-family: "Kaushan Script", cursive; font-size: 120px; line-height: 1.2; color: var(--sale-coral); white-space: nowrap; }
  .sale-status { position: absolute; left: 0; width: 100%; top: 362px; text-align: center; font-family: "Permanent Marker", cursive; font-size: 56px; line-height: 1.2; color: var(--banner-white); white-space: nowrap; letter-spacing: 1px; }
  .sale-decor { position: absolute; left: 0; top: 0; }

  .slide-dots { position: absolute; top: 876px; left: 561px; display: flex; gap: 14px; }
  .slide-dots i { display: block; width: 8px; height: 8px; border-radius: 50%; background: var(--dot); margin-top: 2px; }
  .slide-dots i.current { width: 12px; height: 12px; margin-top: 0; background: transparent; border: 1.5px solid var(--link-soft); }

  .section-title { position: absolute; left: 53px; top: 912px; font-family: "Lora", Georgia, serif; font-size: 30px; font-weight: 400; color: #222; }
  .more-link { position: absolute; right: 54px; top: 920px; font-size: 17px; color: var(--link-soft); text-decoration: none; }

  .category-card { position: absolute; top: 975px; width: 248px; height: 40px; border: 1px solid var(--card-line); border-bottom: none; }
  .category-card .thumb { position: absolute; top: 18px; height: 30px; }
</style>
</head>
<body>
  <header>
    <div class="brand">
      <div class="brand-mark"></div>
      <div class="brand-name"><span class="line-one">Lanternfield</span><span class="line-two">Carpets and Home</span></div>
    </div>
    <div class="account-links">
      <div><strong>Sign in</strong> &nbsp;or&nbsp; <strong>Create an Account</strong></div>
      <div>Call Toll-Free: <strong>1-888-555-LOOM (5666)</strong></div>
    </div>
    <div class="search-field">
      <span>Search all products...</span>
      <svg width="22" height="22" viewBox="0 0 22 22" aria-hidden="true"><circle cx="9" cy="9" r="6.5" fill="none" stroke="#555" stroke-width="2.2"/><line x1="13.8" y1="13.8" x2="20" y2="20" stroke="#555" stroke-width="2.6" stroke-linecap="round"/></svg>
    </div>
    <div class="cart-button">
      <svg width="26" height="20" viewBox="0 0 26 20" aria-hidden="true"><path d="M1 2h4l3 11h13l3-8H7" fill="none" stroke="#666" stroke-width="1.6" stroke-linejoin="round"/><circle cx="10" cy="17" r="1.6" fill="#666"/><circle cx="19" cy="17" r="1.6" fill="#666"/></svg>
      Cart
    </div>
  </header>

  <nav class="main-nav">
    <a href="#">Rugs</a><a href="#">Lighting</a><a href="#">Pillows &amp; Poufs</a><a href="#">Wall Decor</a><a href="#">Table Decor</a><a href="#">Clearance</a><a href="#">Contact Us</a>
  </nav>

  <section class="hero-banner">
    <div class="hero-pattern" role="img" aria-label="Dark hand-knotted rug with a floral pattern in taupe, olive and rust"></div>
    <p class="sale-title">Clearance Sale!</p>
    <p class="sale-status">NOW IN PROGRESS</p>
    <svg class="sale-decor" width="1095" height="548" viewBox="0 0 1095 548" aria-hidden="true">
      <g stroke="#ffffff" stroke-width="3.5" stroke-linecap="round">
        <line x1="247" y1="394" x2="247" y2="420"/><line x1="236" y1="400" x2="258" y2="414"/><line x1="236" y1="414" x2="258" y2="400"/>
        <line x1="892" y1="404" x2="892" y2="430"/><line x1="881" y1="410" x2="903" y2="424"/><line x1="881" y1="424" x2="903" y2="410"/>
      </g>
      <path d="M282 460 Q580 446 866 456" fill="none" stroke="#ffffff" stroke-width="4" stroke-linecap="round"/>
    </svg>
  </section>

  <div class="slide-dots"><i class="current"></i><i></i><i></i><i></i></div>

  <h2 class="section-title">Browse Categories</h2>
  <a class="more-link" href="#">More categories ›</a>

  <div class="category-card" style="left:53px"><div class="thumb" role="img" aria-label="Rug category photo" style="left:30px;width:188px;background:#b7753f"></div></div>
  <div class="category-card" style="left:334px"><div class="thumb" role="img" aria-label="Lighting category photo" style="left:36px;width:176px;background:#a9adb2"></div></div>
  <div class="category-card" style="left:616px"><div class="thumb" role="img" aria-label="Pillows category photo" style="left:112px;width:56px;background:#5c5350"></div></div>
  <div class="category-card" style="left:898px"><div class="thumb" role="img" aria-label="Wall decor category photo" style="left:36px;width:176px;background:#e4e0d6"></div></div>
</body>
</html>
```